Paraffin Wax Packaging Design for Nail and Beauty Industry

We need an attractive design for the packaging of our new product, Paraffin Wax. Our company is a wholesale beauty/nail supply company that has been selling to nail salons in the US market for 10 years. We currently sell this product that we buy from another company. Now we want to launch our own brand of Paraffin Wax.

Target Market(s)

Retail nail salons in the US market.

Industry/Entity Type

Industry

Font styles to use
Sans Serif

Colors

Designer to choose colors to be used in the design.

Requirements
Must have
• Our logo (attached).
• All information on the "Ingredient List" (attached).
• Design for Clear Packaging so product can show through.
• Design for Package Dimensions of 4.25" x 11" (110cm x 280 cm).
Nice to have
• Picture related to women's skin and or beauty.
• Contrast as in the design of product that we currently sell (attached).

```html
<!DOCTYPE html>
<html lang="en">
<head>
<meta charset="utf-8">
<title>Paraffin Wax Pouch</title>
<link href="https://fonts.googleapis.com/css2?family=Cinzel:wght@400&family=Source+Sans+3:wght@400;600;700&display=swap" rel="stylesheet">
<style>
  :root {
    --page-bg: #ffffff;
    --pouch-bg: #e4e4e4;
    --magenta: #e6287f;
    --flower-deep: #e0157f;
    --flower-light: #f06aa8;
    --flower-pale: #f6a9c9;
    --ink: #111111;
  }
  html, body {
    margin: 0;
    width: 1200px;
    height: 1200px;
    overflow: hidden;
    background: var(--page-bg);
  }
  .canvas {
    position: relative;
    width: 1200px;
    height: 1200px;
  }
  .pouch {
    position: absolute;
    left: 414px;
    top: 120px;
    width: 371px;
    height: 960px;
    background: var(--pouch-bg);
    overflow: hidden;
  }
  .floral {
    position: absolute;
    left: 0;
    top: 0;
    width: 371px;
    height: 960px;
  }
  .product-title {
    position: absolute;
    right: 48px;
    top: 222px;
    margin: 0;
    font-family: "Cinzel", serif;
    font-weight: 400;
    font-size: 40px;
    line-height: 38px;
    color: var(--magenta);
    text-align: right;
    letter-spacing: 0.5px;
  }
  .copy {
    position: absolute;
    left: 62px;
    width: 258px;
    margin: 0;
    font-family: "Source Sans 3", sans-serif;
    font-size: 19px;
    line-height: 20.8px;
    color: var(--magenta);
    text-align: justify;
  }
  .copy--bold { font-weight: 600; }
  .copy--regular { font-weight: 400; }
  .copy .label { font-weight: 700; }
  .compat { top: 312px; }
  .benefit { top: 394px; }
  .ingredients { top: 476px; }
  .caution { top: 578px; }
  .brand {
    position: absolute;
    left: 86px;
    top: 664px;
    margin: 0;
    font-family: "Source Sans 3", sans-serif;
    font-weight: 600;
    font-size: 36px;
    color: var(--ink);
    display: flex;
    align-items: center;
    gap: 10px;
  }
  .brand-dot {
    width: 12px;
    height: 12px;
    border-radius: 50%;
    background: var(--ink);
  }
  .net-weight {
    position: absolute;
    right: 26px;
    bottom: 20px;
    margin: 0;
    font-family: "Source Sans 3", sans-serif;
    font-weight: 600;
    font-size: 16px;
    color: var(--ink);
  }
</style>
</head>
<body>
<div class="canvas">
  <div class="pouch">
    <svg class="floral" viewBox="0 0 371 960" xmlns="http://www.w3.org/2000/svg">
      <defs>
        <linearGradient id="floralTop" x1="0" y1="0" x2="1" y2="1">
          <stop offset="0" stop-color="var(--flower-deep)"/>
          <stop offset="0.6" stop-color="var(--flower-light)"/>
          <stop offset="1" stop-color="var(--flower-pale)"/>
        </linearGradient>
        <linearGradient id="floralBottom" x1="1" y1="1" x2="0" y2="0">
          <stop offset="0" stop-color="var(--flower-deep)"/>
          <stop offset="0.6" stop-color="var(--flower-light)"/>
          <stop offset="1" stop-color="var(--flower-pale)"/>
        </linearGradient>
      </defs>
      <polygon role="img" aria-label="Cluster of pink and magenta flowers across the top corner"
        fill="url(#floralTop)"
        points="0,0 371,0 371,40 325,88 268,118 210,148 160,188 120,228 95,268 58,298 38,338 18,368 0,378"/>
      <polygon role="img" aria-label="Cluster of pink and magenta flowers in the bottom corner"
        fill="url(#floralBottom)"
        points="371,640 350,680 338,722 300,762 240,800 200,830 140,862 80,890 30,910 0,920 0,960 371,960"/>
    </svg>

    <h1 class="product-title">Paraffin<br>Wax</h1>

    <p class="copy copy--bold compat">Compatible for use with most wax paraffin heat therapy units.</p>
    <p class="copy copy--bold benefit">Deeply Moisturizes the Skin Restoring a Healthier Look and Feel to Skin.</p>
    <p class="copy copy--regular ingredients"><span class="label">Ingredients:</span> Paraffin waxes and Hydrocarbon waxes, Petrolatum, Paraffin oils, Apricot kernel oil, Fragrance D &amp; C dyes.</p>
    <p class="copy copy--regular caution"><span class="label">Caution:</span> Paraffin is flammable. Do not use near open flame or an unprotected resistance heater.</p>

    <p class="brand"><span class="brand-dot"></span>By Lumira</p>

    <p class="net-weight">Net Wt. 1 lb. (450 g.)</p>
  </div>
</div>
</body>
</html>
```